Personal Business Card Design Project

I require a two sided personal business card design.

I am a 35 year old Angel Investor and I invest in various niche internet and F&B projects in China. I am Chinese Australian

One side should be in English and the other side should be in Chinese.

My English details are:

Cole Marsh
Angel Investor

China: +86 1390 274 5183
Hong Kong: +852 6133 4087
Email: cole@cdmarsh.net
Address: Flat 2407, Block 5, Pinecrest Gardens,
42 Maoyuan Road (near Beiling Road),
Shanghai, 200437,
China

My Chinese details are (do not print the text in brackets)

袁哲明 (Name)
天使投资者(Angel Investor)

中国 (China): +86 1390 274 5183
香港 (Hong Kong): +852 6133 4087
Email: cole@cdmarsh.net
地址 (Address): 上海市茂园路42号5号楼2407室
松岭花园, 中国 200437

Target Market(s)

I will only give this card to present to new partners and suppliers and people asking for funding. Not customers.

Industry/Entity Type

Internet

Requirements
Must have
• Something a little humourous in terms of graphics that suggest helping something to grow since I invest in startups. But I want a sophisticated look to it as well.
Nice to have
• Black and White tongue in cheek graphics but not overboard.

The whole card can be not conventional in shape or have cutouts but still retain the business standard business card size.

```html
<!DOCTYPE html>
<html lang="zh">
<head>
<meta charset="utf-8">
<title>袁哲明 — 天使投资者</title>
<link rel="stylesheet" href="https://fonts.googleapis.com/css2?family=Open+Sans:wght@400&family=Noto+Sans+SC:wght@300;400&display=swap">
<style>
  :root {
    --card-red: #ed1c24;
    --card-white: #ffffff;
    --title-grey: #7b7b7b;
    --outline-grey: #d4d4d4;
    --page-bg: #ffffff;
  }
  html, body {
    margin: 0;
    padding: 0;
    width: 1200px;
    height: 895px;
    overflow: hidden;
    background: var(--page-bg);
  }
  .business-card {
    display: block;
    width: 1200px;
    height: 895px;
  }
  .card-shape {
    fill: var(--card-white);
    stroke: var(--outline-grey);
    stroke-width: 1.5;
  }
  .speech-bubble { fill: var(--card-red); }
  .icon { fill: var(--card-white); }
  .icon-line {
    fill: none;
    stroke: var(--card-red);
    stroke-width: 2;
  }
  .contact-text {
    fill: var(--card-white);
    font-family: "Open Sans", "Noto Sans SC", sans-serif;
    font-size: 21px;
  }
  .contact-label {
    font-family: "Noto Sans SC", sans-serif;
    font-size: 15px;
  }
  .address-text {
    font-family: "Noto Sans SC", "Open Sans", sans-serif;
    font-size: 21px;
  }
  .holder-name {
    fill: var(--card-red);
    font-family: "Noto Sans SC", sans-serif;
    font-weight: 400;
    font-size: 58px;
  }
  .holder-title {
    fill: var(--title-grey);
    font-family: "Noto Sans SC", sans-serif;
    font-weight: 300;
    font-size: 48px;
  }
</style>
</head>
<body>
<svg class="business-card" viewBox="0 0 1200 895" xmlns="http://www.w3.org/2000/svg" aria-label="名片：袁哲明，天使投资者">
  <!-- Die-cut card outline with rounded crown -->
  <path class="card-shape" d="M72 347 H470 A282 226 0 0 1 1005 347 H1120 V780 H72 Z"/>

  <!-- Red speech bubble -->
  <g class="speech-bubble">
    <ellipse cx="737" cy="423" rx="267" ry="208"/>
    <polygon points="545,555 512,632 600,598"/>
  </g>

  <!-- Phone icon -->
  <g class="icon icon-phone">
    <path d="M574 312 c-8 6 -10 18 -4 30 c10 18 24 30 42 26 l8 -6 l-12 -12 l-8 4 c-8 -4 -14 -12 -16 -20 l6 -6 z"/>
    <rect x="607" y="347" width="10" height="8" rx="2" transform="rotate(45 612 351)"/>
    <rect x="572" y="310" width="10" height="8" rx="2" transform="rotate(45 577 314)"/>
  </g>

  <!-- Envelope icon -->
  <g class="icon-mail">
    <rect class="icon" x="566" y="394" width="62" height="39"/>
    <polyline class="icon-line" points="567,395 597,418 627,395"/>
    <line class="icon-line" x1="567" y1="432" x2="588" y2="412"/>
    <line class="icon-line" x1="627" y1="432" x2="606" y2="412"/>
  </g>

  <!-- House icon -->
  <g class="icon icon-home">
    <polygon points="598,469 568,501 574,501 598,476 622,501 628,501"/>
    <rect x="608" y="474" width="7" height="14"/>
    <path d="M576 504 L598 482 L620 504 V533 H606 V512 H590 V533 H576 Z"/>
  </g>

  <!-- Contact details -->
  <text class="contact-text" text-anchor="end" x="935" y="333"><tspan class="contact-label">中国</tspan>  +86 1390 274 5183</text>
  <text class="contact-text" text-anchor="end" x="935" y="361"><tspan class="contact-label">香港</tspan> +852 6133 4087</text>
  <text class="contact-text" text-anchor="end" x="935" y="419">cole@cdmarsh.net</text>
  <text class="contact-text address-text" text-anchor="end" x="935" y="477">上海市茂园路</text>
  <text class="contact-text address-text" text-anchor="end" x="935" y="505">42号5号楼2407室</text>
  <text class="contact-text address-text" text-anchor="end" x="935" y="533">松岭花园, 中国 200437</text>

  <!-- Name and title -->
  <text class="holder-name" x="108" y="745">袁哲明</text>
  <text class="holder-title" x="375" y="744">天使投资者</text>
</svg>
</body>
</html>
```